Criação de Papelaria (6 itens) para Arquitetura
" Sou recém formada em Design de Interiores e pretendo começar a divulgar meu negócio. Já fiz alguns trabalhos / projetos, mas ainda não consegui alavancar minha marca. Meu foco será a realização de projetos residenciais, comerciais e empresariais. As atividades vão desde a entrevista inicial para entendimento das necessidades do cliente, passando pela preparação dos projetos com imagens renderizadas, plantas baixas, projetos de marcenaria, iluminação, gesso etc., incluindo também acompanhamento a lojas para escolha de materiais / móveis até o acompanhamento da obra e fiscalização dos trabalhos executados por terceiros. "

```html
<!DOCTYPE html>
<html lang="pt-BR">
<head>
<meta charset="utf-8">
<title>Lia Moreno — Papel Timbrado</title>
<link href="https://fonts.googleapis.com/css2?family=Montserrat:wght@300;400&display=swap" rel="stylesheet">
<style>
  :root {
    --bg: #e4e4e6;
    --paper: #ffffff;
    --rose: #e6a497;
    --rose-soft: #f3d3cb;
    --ink: #3b3b42;
    --ink-soft: #6a6a72;
    --watermark: #f1f1f3;
  }
  html, body {
    margin: 0;
    width: 1200px;
    height: 1200px;
    overflow: hidden;
    background: var(--bg);
    font-family: "Montserrat", sans-serif;
  }
  .letterhead {
    position: absolute;
    left: 211px;
    top: 50px;
    width: 778px;
    height: 1100px;
    background: var(--paper);
    box-shadow: 0 6px 24px rgba(0,0,0,0.12);
    overflow: hidden;
  }
  .brand {
    position: absolute;
    top: 52px;
    left: 0;
    right: 0;
    text-align: center;
    color: var(--ink);
  }
  .brand-name {
    display: inline-flex;
    align-items: center;
    gap: 12px;
    font-weight: 300;
    font-size: 30px;
    letter-spacing: 6px;
  }
  .brand-mark {
    width: 14px;
    height: 14px;
    background: var(--rose);
  }
  .brand-tagline {
    margin-top: 6px;
    font-weight: 300;
    font-size: 10px;
    letter-spacing: 5px;
    color: var(--ink-soft);
  }
  .header-band {
    position: absolute;
    top: 78px;
    height: 10px;
    background: linear-gradient(90deg, var(--rose-soft), var(--rose), var(--rose-soft));
    opacity: 0.8;
  }
  .header-band.left { left: 0; width: 250px; }
  .header-band.right { right: 0; width: 250px; }
  .watermark {
    position: absolute;
    top: 430px;
    left: 0;
    right: 0;
    text-align: center;
    font-weight: 400;
    font-size: 92px;
    letter-spacing: 10px;
    color: var(--watermark);
  }
  .contact {
    position: absolute;
    bottom: 38px;
    left: 60px;
    right: 60px;
    display: flex;
    justify-content: space-between;
    font-size: 10px;
    color: var(--ink-soft);
    line-height: 1.5;
  }
  .contact-item {
    display: flex;
    align-items: center;
    gap: 8px;
  }
  .contact-icon {
    width: 20px;
    height: 20px;
    flex: none;
  }
  .footer-rule {
    position: absolute;
    left: 0;
    right: 0;
    bottom: 0;
    height: 10px;
    background: var(--ink);
  }
  .footer-rule::before {
    content: "";
    position: absolute;
    left: 0;
    right: 0;
    top: -4px;
    height: 2px;
    background: var(--rose);
  }
</style>
</head>
<body>
  <main class="letterhead">
    <div class="header-band left" role="img" aria-label="Faixa decorativa em padrão de elos rosé"></div>
    <div class="header-band right" role="img" aria-label="Faixa decorativa em padrão de elos rosé"></div>

    <header class="brand">
      <div class="brand-name"><span class="brand-mark"></span>LIA MORENO</div>
      <div class="brand-tagline">DESIGN DE INTERIORES</div>
    </header>

    <div class="watermark" aria-hidden="true">LIA MORENO</div>

    <footer class="contact">
      <div class="contact-item">
        <svg class="contact-icon" viewBox="0 0 20 20"><circle cx="10" cy="10" r="10" fill="#3b3b42"/><path d="M10 4.5a3.5 3.5 0 0 0-3.5 3.5c0 2.6 3.5 7 3.5 7s3.5-4.4 3.5-7A3.5 3.5 0 0 0 10 4.5zm0 4.8a1.3 1.3 0 1 1 0-2.6 1.3 1.3 0 0 1 0 2.6z" fill="#fff"/></svg>
        <div>Rua das Acácias, 120<br>CEP 00000-000 · Cidade</div>
      </div>
      <div class="contact-item">
        <svg class="contact-icon" viewBox="0 0 20 20"><circle cx="10" cy="10" r="10" fill="#3b3b42"/><path d="M7 5.5l2 2.2-1 1.3a7 7 0 0 0 3 3l1.3-1 2.2 2-1 1.5c-3.5 0-7.5-4-7.5-7.5z" fill="#fff"/></svg>
        <div>(11) 0000-0000<br>(11) 90000-0000</div>
      </div>
      <div class="contact-item">
        <svg class="contact-icon" viewBox="0 0 20 20"><circle cx="10" cy="10" r="10" fill="#3b3b42"/><circle cx="10" cy="10" r="5" fill="none" stroke="#fff" stroke-width="1"/><path d="M5 10h10M10 5c-2 2.8-2 7.2 0 10M10 5c2 2.8 2 7.2 0 10" fill="none" stroke="#fff" stroke-width="1"/></svg>
        <div>www.liamoreno.com<br>contato@liamoreno.com</div>
      </div>
    </footer>
    <div class="footer-rule"></div>
  </main>
</body>
</html>
```